Door Company Flyer for October Hardware Sale

We are a door company and need a new flyer for a sale on hardware going on starting today thru the end of October (Oct 1st-Oct 31st) Our logo colors are gray, orange, and white. We need the 3 pictures of hardware included. Our company is TOLVAN Commercial Door, our supplier is Marquith and the hardware on sale is Bristow brand. We will need this in pdf format to print flyers and also a digital version to post on our website and social media.

```html
<!DOCTYPE html>
<html lang="en">
<head>
<meta charset="utf-8">
<title>TOLVAN Commercial Door – October Sale Flyer</title>
<link href="https://fonts.googleapis.com/css2?family=Montserrat:wght@300;600;700;800;900&display=swap" rel="stylesheet">
<style>
  :root {
    --orange: #f7941d;
    --gray: #939598;
    --gray-light: #d9dadb;
    --ink: #262626;
    --backdrop: #333333;
    --white: #ffffff;
  }
  * { margin: 0; padding: 0; box-sizing: border-box; }
  html, body { width: 1200px; height: 1200px; overflow: hidden; background: var(--backdrop); }
  body { font-family: "Montserrat", Arial, sans-serif; position: relative; }

  .flyer { position: absolute; left: 217px; top: 63px; width: 766px; height: 1074px; background: var(--white); overflow: hidden; }
  .flyer > * { position: absolute; }

  .brand-name { left: 0; width: 766px; top: 52px; text-align: center; color: var(--gray); font-weight: 800; line-height: 1; }
  .brand-name .word { display: block; font-size: 58px; letter-spacing: 4px; }
  .brand-name .sub { display: block; font-size: 17px; letter-spacing: 2px; margin-top: 6px; }

  .ribbon { left: 69px; top: 181px; width: 633px; height: 92px; }
  .ribbon-title { left: 117px; top: 181px; width: 538px; height: 72px; text-align: center; color: var(--white); font-weight: 700; font-size: 66px; line-height: 72px; letter-spacing: -0.5px; white-space: nowrap; }

  .headline { left: 0; width: 766px; text-align: center; font-weight: 900; line-height: 1; white-space: nowrap; }
  .headline-main { top: 289px; color: var(--orange); font-size: 47px; letter-spacing: -0.3px; }
  .headline-sub { top: 355px; color: var(--gray); font-size: 40px; }

  .date-rule { left: 196px; width: 376px; height: 3px; background: var(--orange); }
  .date-rule.top { top: 409px; }
  .date-rule.bottom { top: 474px; }
  .sale-dates { left: 196px; width: 376px; top: 419px; text-align: center; color: var(--gray); font-weight: 300; font-size: 47px; line-height: 1.1; white-space: nowrap; }

  .product-stage { left: 0; top: 495px; width: 766px; height: 260px; }
  .product { border-radius: 6px; background: linear-gradient(160deg, #e4e5e7, #b9bbbe); }
  .product.closer { left: 27px; top: 612px; width: 204px; height: 130px; }
  .product.lever-lock { left: 289px; top: 513px; width: 208px; height: 144px; background: linear-gradient(160deg, #e6e7e8, #c2b48a); }
  .product.exit-device { left: 510px; top: 575px; width: 223px; height: 152px; }

  .brands-heading { left: 0; width: 766px; top: 771px; display: flex; justify-content: center; align-items: center; gap: 16px; }
  .brands-heading h2 { color: var(--gray); font-weight: 900; font-size: 37px; line-height: 1; white-space: nowrap; }
  .menu-bars { width: 29px; height: 31px; display: flex; flex-direction: column; justify-content: space-between; }
  .menu-bars span { display: block; height: 6px; background: var(--orange); }

  .brand-card { top: 821px; width: 317px; height: 102px; border: 1.5px solid var(--gray); display: flex; background: var(--white); }
  .brand-card.supplier { left: 50px; }
  .brand-card.hardware { left: 400px; }
  .brand-card .role { width: 158px; background: var(--gray); color: var(--white); font-weight: 800; font-size: 23px; display: flex; align-items: center; justify-content: center; }
  .brand-card .partner { flex: 1; display: flex; align-items: center; justify-content: center; color: var(--ink); font-weight: 800; font-size: 22px; letter-spacing: 0.5px; white-space: nowrap; }

  .footer { left: 0; top: 939px; width: 766px; height: 135px; background: var(--orange); }
  .footer > * { position: absolute; }
  .footer-rule { left: 0; top: 8px; width: 766px; height: 1.5px; background: var(--white); }
  .estimate-tab { left: 120px; top: 10px; width: 525px; height: 41px; }
  .estimate-text { left: 120px; top: 10px; width: 525px; height: 41px; text-align: center; color: var(--orange); font-weight: 700; font-size: 28px; line-height: 41px; white-space: nowrap; }

  .contact-row { left: 23px; top: 78px; height: 34px; display: flex; align-items: center; color: var(--white); font-weight: 600; font-size: 20px; white-space: nowrap; }
  .contact-item { display: flex; align-items: center; gap: 7px; }
  .contact-item + .contact-item { margin-left: 28px; }
  .divider { width: 1.5px; height: 32px; background: var(--white); margin: 0 20px 0 24px; }
  .social { display: flex; gap: 11px; }
  .social span { width: 32px; height: 32px; border-radius: 50%; background: var(--white); display: block; }
</style>
</head>
<body>
  <main class="flyer">
    <div class="brand-name"><span class="word">TOLVAN</span><span class="sub">COMMERCIAL DOOR</span></div>

    <svg class="ribbon" viewBox="0 0 633 92" aria-hidden="true">
      <polygon points="0,20 48,20 48,72 81,72 81,92 0,92 37,56" fill="var(--gray)"/>
      <polygon points="633,20 585,20 585,72 553,72 553,92 633,92 596,56" fill="var(--gray)"/>
      <rect x="48" y="0" width="538" height="72" fill="var(--orange)"/>
    </svg>
    <div class="ribbon-title">October Sale</div>

    <div class="headline headline-main">High-Quality Commercial</div>
    <div class="headline headline-sub">Doors and Hardware</div>

    <div class="date-rule top"></div>
    <div class="sale-dates">Oct 1st-Oct 31st</div>
    <div class="date-rule bottom"></div>

    <svg class="product-stage" viewBox="0 0 766 260" aria-hidden="true">
      <defs>
        <linearGradient id="stageShade" x1="0" y1="0" x2="0" y2="1">
          <stop offset="0" stop-color="#ffffff"/>
          <stop offset="1" stop-color="#e3e4e5"/>
        </linearGradient>
      </defs>
      <polygon points="136,10 373,246 634,10 373,252" fill="url(#stageShade)"/>
      <polyline points="136,10 373,246 634,10" fill="none" stroke="#d4d5d7" stroke-width="1.5"/>
    </svg>

    <div class="product closer" role="img" aria-label="Photo of a silver overhead door closer"></div>
    <div class="product lever-lock" role="img" aria-label="Photo of a satin chrome lever lockset"></div>
    <div class="product exit-device" role="img" aria-label="Photo of two silver push bar exit devices"></div>

    <div class="brands-heading">
      <div class="menu-bars"><span></span><span></span><span></span></div>
      <h2>Notable Brands We Carry</h2>
      <div class="menu-bars"><span></span><span></span><span></span></div>
    </div>

    <div class="brand-card supplier">
      <div class="role">Supplier</div>
      <div class="partner">MARQUITH</div>
    </div>
    <div class="brand-card hardware">
      <div class="role">Hardware</div>
      <div class="partner">BRISTOW</div>
    </div>

    <footer class="footer">
      <div class="footer-rule"></div>
      <svg class="estimate-tab" viewBox="0 0 525 41" aria-hidden="true">
        <polygon points="0,0 525,0 511,41 14,41" fill="var(--white)"/>
      </svg>
      <div class="estimate-text">Contact Us for a Free Estimate</div>

      <div class="contact-row">
        <div class="contact-item">
          <svg width="20" height="20" viewBox="0 0 24 24" aria-hidden="true">
            <path d="M6.6 10.8a15 15 0 0 0 6.6 6.6l2.2-2.2a1 1 0 0 1 1-.25 11.4 11.4 0 0 0 3.6.57 1 1 0 0 1 1 1V20a1 1 0 0 1-1 1A17 17 0 0 1 3 4a1 1 0 0 1 1-1h3.5a1 1 0 0 1 1 1c0 1.25.2 2.45.57 3.57a1 1 0 0 1-.25 1z" fill="var(--white)"/>
          </svg>
          <span>(555) 214-0387</span>
        </div>
        <div class="contact-item">
          <svg width="26" height="17" viewBox="0 0 26 17" aria-hidden="true">
            <rect x="1" y="1" width="24" height="15" fill="none" stroke="var(--white)" stroke-width="2"/>
            <polyline points="1,1 13,10 25,1" fill="none" stroke="var(--white)" stroke-width="2"/>
          </svg>
          <span>sales@tolvancommercialdoor.com</span>
        </div>
        <div class="divider"></div>
        <div class="social"><span></span><span></span></div>
      </div>
    </footer>
  </main>
</body>
</html>
```